Book Cover for a technology book - The Silent Lattice

We are writing a book that is a handbook how to build a hybrid cloud - this is a technology concept where companies use cloud services both from the like of Vornix or Plenquor and also cloud services built in there own data centers - hence the term hybrid cloud. We want a book cover with the title - The Silent Lattice; which signifies that we will be teaching companies how to build a hybrid cloud that just works. We want the tagline - handbook for building Hybrid Clouds. The authors are Corwin Haddle and Ross Pelley. The cover is to be engaging and feel different than your usual technical manual. I don't have any graphics to help out however will be able to refine and tell you what I don and don't like based on your drafts. The book dimensions are yet to be determined, in the first instance it will be a PDF

Target Market(s)

technology executives and specialists

Industry/Entity Type

Information Technology

Colors

Designer to choose colors to be used in the design.

Requirements
Nice to have
• While I don't have a particular view to how it will look, I'd like the style to be more casual than ultra formal

```html
<!DOCTYPE html>
<html lang="en">
<head>
<meta charset="utf-8">
<title>The Silent Lattice — Book Cover</title>
<link href="https://fonts.googleapis.com/css2?family=Open+Sans:wght@300;400;700;800&display=swap" rel="stylesheet">
<style>
  :root {
    --cover-blue: #1b5d86;
    --ink-white: #ffffff;
    --title-shadow: rgba(8, 30, 48, 0.75);
    --cloud-light: #e6eef3;
    --cloud-mid: #b7c9d6;
    --cloud-deep: #7f9aae;
  }
  html, body {
    margin: 0;
    padding: 0;
    overflow: hidden;
    background: var(--cover-blue);
  }
  .book-cover {
    position: relative;
    width: 800px;
    height: 1200px;
    background: var(--cover-blue);
    overflow: hidden;
    font-family: "Open Sans", sans-serif;
    color: var(--ink-white);
  }
  .cover-title {
    position: absolute;
    top: 128px;
    left: 0;
    width: 800px;
    margin: 0;
    text-align: center;
    font-weight: 800;
    text-transform: uppercase;
    text-shadow: 4px 6px 6px var(--title-shadow);
    white-space: nowrap;
  }
  .cover-title .title-line-small {
    display: block;
    font-size: 104px;
    line-height: 112px;
    letter-spacing: 1px;
  }
  .cover-title .title-line-large {
    display: block;
    font-size: 132px;
    line-height: 164px;
    letter-spacing: -1px;
    margin-top: 4px;
  }
  .cover-tagline {
    position: absolute;
    top: 460px;
    left: 0;
    width: 800px;
    margin: 0;
    text-align: center;
    font-weight: 400;
    font-size: 27px;
    letter-spacing: 0.3px;
    text-transform: uppercase;
  }
  .cover-art {
    position: absolute;
    top: 590px;
    left: 95px;
    width: 610px;
    height: 410px;
  }
  .cover-authors {
    position: absolute;
    top: 1092px;
    left: 0;
    width: 800px;
    margin: 0;
    text-align: center;
    font-weight: 700;
    font-size: 35px;
    letter-spacing: 0.5px;
    text-transform: uppercase;
  }
</style>
</head>
<body>
  <main class="book-cover">
    <h1 class="cover-title">
      <span class="title-line-small">The Silent</span>
      <span class="title-line-large">Lattice</span>
    </h1>
    <p class="cover-tagline">Handbook for building Hybrid Clouds</p>

    <svg class="cover-art" viewBox="0 0 610 410" role="img" aria-label="Illustration of a soft white cloud overlaid with a network of connected nodes and lines">
      <defs>
        <radialGradient id="cloudFill" cx="50%" cy="50%" r="55%">
          <stop offset="0%" stop-color="var(--cloud-mid)"/>
          <stop offset="55%" stop-color="var(--cloud-light)"/>
          <stop offset="85%" stop-color="var(--cloud-deep)" stop-opacity="0.6"/>
          <stop offset="100%" stop-color="var(--cloud-deep)" stop-opacity="0"/>
        </radialGradient>
        <filter id="cloudSoften" x="-10%" y="-10%" width="120%" height="120%">
          <feGaussianBlur stdDeviation="12"/>
        </filter>
      </defs>
      <ellipse cx="305" cy="205" rx="290" ry="190" fill="url(#cloudFill)" filter="url(#cloudSoften)"/>
    </svg>

    <p class="cover-authors">Corwin Haddle and Ross Pelley</p>
  </main>
</body>
</html>
```